Poetry Book Cover Design Project

Looking for a minimalistic book cover design for a collection of poems. The book title is "Before The Morning Turns To Glass". There are three parts to the book. First covers poetry in the theme of Rage. Second love and desire. The third is strange poems. Essentially the sections are "Rage", "Desire" and the "Strange". The reason for the title "Before The Morning Turns To Glass" is as if someone is writing these till life changes towards the intended outcome as felt in each poem. I want to have the author's name "Nirosha Kulathunge" at the bottom. Ilustration attached.
- Minimalistic

```html
<!DOCTYPE html>
<html lang="en">
<head>
<meta charset="utf-8">
<title>Before The Morning Turns To Glass — Book Cover</title>
<link rel="stylesheet" href="https://fonts.googleapis.com/css2?family=Libre+Caslon+Display&family=Marcellus&display=swap">
<style>
  :root {
    --backdrop: #e8e3de;
    --cover: #fbfbfa;
    --ink: #0b0b0b;
    --paper-text: #f4f4f4;
  }
  html, body {
    margin: 0;
    width: 1200px;
    height: 800px;
    overflow: hidden;
    background: var(--backdrop);
  }
  .stage {
    width: 1200px;
    height: 800px;
    display: flex;
    align-items: center;
    justify-content: center;
  }
  .book-cover {
    position: relative;
    width: 480px;
    height: 720px;
    background: var(--cover);
    box-shadow: 0 2px 14px rgba(0, 0, 0, 0.08);
    overflow: hidden;
  }
  .top-band {
    position: absolute;
    top: 0;
    left: 50%;
    transform: translateX(-50%);
    width: 216px;
    height: 50px;
    background: var(--ink);
  }
  .title {
    position: absolute;
    top: 92px;
    left: 0;
    right: 0;
    margin: 0;
    text-align: center;
    font-family: "Libre Caslon Display", serif;
    font-weight: 400;
    color: var(--ink);
    line-height: 0.86;
    letter-spacing: -0.01em;
  }
  .title span { display: block; }
  .title .w-before  { font-size: 118px; }
  .title .w-the     { font-size: 92px; }
  .title .w-morning { font-size: 88px; }
  .title .w-turns   { font-size: 60px; }
  .title .w-to      { font-size: 96px; }
  .title .w-glass   { font-size: 104px; }
  .author-plate {
    position: absolute;
    bottom: 18px;
    left: 50%;
    transform: translateX(-50%);
    width: 230px;
    height: 112px;
    background: var(--ink);
    display: flex;
    flex-direction: column;
    align-items: center;
    justify-content: center;
    gap: 6px;
  }
  .author-name {
    margin: 0;
    font-family: "Marcellus", serif;
    font-size: 15px;
    letter-spacing: 0.26em;
    text-transform: uppercase;
    color: var(--paper-text);
    text-align: center;
    line-height: 1.35;
  }
</style>
</head>
<body>
  <main class="stage">
    <article class="book-cover">
      <div class="top-band"></div>
      <h1 class="title">
        <span class="w-before">Before</span>
        <span class="w-the">The</span>
        <span class="w-morning">Morning</span>
        <span class="w-turns">Turns</span>
        <span class="w-to">To</span>
        <span class="w-glass">Glass</span>
      </h1>
      <div class="author-plate">
        <p class="author-name">Nirosha<br>Kulathunge</p>
      </div>
    </article>
  </main>
</body>
</html>
```